Signage for a foam car wash facility

We need signages done for a foam car wash.
We use only premium, environment-friendly, biodegradable foam wash and cleaning products.
We are in a commercial center (mall) situated in an upscale part of town and need our signage to reflect that.
We need signages for directions (two or three smaller ones), one showing that we are here, and at the actual car wash.
We will provide our logo, the texts, some pictures of the actual location the dimensions of the signages.
We need the signages to be informative, clean, crisp, modern with the use of icons if possible and some colour so that we get the attention of clients passing -by without being too flashy.
Directions to the car wash should look like a petal of a flower directing towards the car wash

Target Market(s)

Upscale market with a school and a gym next to it. Mom and dad's dropping their children at school, offices nearby.

Industry/Entity Type

Car Wash

Requirements
Nice to have
• icons, some colors,Directions to the car wash should look like a petal of a flower directing towards the car wash

```html
<!DOCTYPE html>
<html lang="en">
<head>
<meta charset="utf-8">
<title>Foam Car Wash – Direction Signs</title>
<link rel="stylesheet" href="https://fonts.googleapis.com/css2?family=Barlow+Condensed:ital,wght@0,700;1,800&family=Montserrat:wght@400&display=swap">
<style>
  :root {
    --navy: #1d4e89;
    --lime: #b5c93c;
    --white: #ffffff;
    --paper: #ffffff;
    --frame: #6b6b6b;
    --label: #333333;
    --car-area: #2b5e98;
  }
  html, body {
    margin: 0;
    padding: 0;
    width: 1200px;
    height: 717px;
    overflow: hidden;
    background: var(--paper);
  }
  .sheet {
    position: relative;
    width: 1200px;
    height: 717px;
    display: flex;
    justify-content: center;
  }
  .sign-board { width: 597px; height: 717px; display: block; }
  .dimension-label {
    font-family: "Montserrat", sans-serif;
    font-size: 26px;
    fill: var(--label);
  }
  .artboard-frame { fill: none; stroke: var(--frame); stroke-width: 1.2; }
  .petal { fill: var(--navy); }
  .arrow { fill: var(--lime); }
  .headline {
    font-family: "Barlow Condensed", sans-serif;
    font-weight: 700;
    font-size: 60px;
    fill: var(--white);
  }
  .service-name {
    font-family: "Barlow Condensed", sans-serif;
    font-style: italic;
    font-weight: 800;
    font-size: 84px;
    fill: var(--navy);
  }
  .brand-name {
    font-family: "Barlow Condensed", sans-serif;
    font-weight: 700;
    font-size: 44px;
    letter-spacing: 1px;
    fill: var(--lime);
  }
  .brand-dot { fill: var(--lime); }
  .car-icon-area { fill: var(--car-area); }
</style>
</head>
<body>
<main class="sheet">
  <svg class="sign-board" viewBox="0 0 880 1057" xmlns="http://www.w3.org/2000/svg">
    <!-- Dimensions -->
    <text class="dimension-label" x="471" y="90" text-anchor="middle">40 cm</text>
    <text class="dimension-label" x="0" y="0" text-anchor="middle" transform="translate(66 307) rotate(-90)">20 cm</text>

    <!-- Right-pointing sign -->
    <g class="sign sign--right">
      <rect class="artboard-frame" x="89" y="114" width="764" height="387"/>
      <path class="petal" d="M240,114 L600,114 Q680,114 722,168 L850,307 L705,440 Q645,500 560,500 L240,500 C140,500 90,400 90,307 C90,200 140,114 240,114 Z"/>
      <path class="arrow" d="M383,253 L693,253 L693,210 L818,307 L693,403 L693,362 L383,362 A54.5,54.5 0 0 1 383,253 Z"/>
      <text class="headline" x="158" y="231">PREMIUM ECO-FRIENDLY</text>
      <text class="service-name" x="354" y="337">CAR WASH</text>
      <rect class="car-icon-area" x="138" y="250" width="208" height="215" rx="40" role="img" aria-label="Line icon of a car covered in wash foam"/>
      <circle class="brand-dot" cx="344" cy="438" r="20"/>
      <text class="brand-name" x="380" y="455">AQUAVERT</text>
    </g>

    <!-- Left-pointing sign -->
    <g class="sign sign--left">
      <rect class="artboard-frame" x="89" y="591" width="764" height="387"/>
      <path class="petal" transform="translate(943 477) scale(-1 1)" d="M240,114 L600,114 Q680,114 722,168 L850,307 L705,440 Q645,500 560,500 L240,500 C140,500 90,400 90,307 C90,200 140,114 240,114 Z"/>
      <path class="arrow" d="M558,730 L245,730 L245,687 L120,783 L245,880 L245,838 L558,838 A54,54 0 0 0 558,730 Z"/>
      <text class="headline" x="262" y="707">PREMIUM ECO-FRIENDLY</text>
      <text class="service-name" x="256" y="812">CAR WASH</text>
      <rect class="car-icon-area" x="592" y="727" width="208" height="215" rx="40" role="img" aria-label="Line icon of a car covered in wash foam, facing left"/>
      <circle class="brand-dot" cx="354" cy="908" r="20"/>
      <text class="brand-name" x="390" y="925">AQUAVERT</text>
    </g>
  </svg>
</main>
</body>
</html>
```